redesign corporate website (software courses)

We need a complete redesign of the current website: http://t-o-m.example/ (training: http://t-o-m.example/pt-br/treinamento/web ); more clear, different color, navigation, header, footer, whatever (side note: site will be based on bootstrap and drupal). Most important pages:

http://t-o-m.example/pt-br/treinamento (trainingoverviewpage)
http://t-o-m.example/ (frontpage)
http://t-o-m.example/pt-br/treinamento/web (trianingdetailpage)

The design should be valid for further content pages (like http://t-o-m.example/pt-br/desenvolvimentodesoftware) and pages with forms (http://t-o-m.example/pt-br/contact or http://t-o-m.example/pt-br/training/web/register)

Logo attached in white and black and black with shadow.

Some other examples of training sites (just content examples - not as template for similar layout):

http://www.brivatutor.example/packages/4817/Website-Development-Professional-training.html?advid=12&gclid=XQa93kLpr42DFbvn3BqeWTZBqk
http://www.kodewerk-kurse.example/
http://www.lumacod.example/cursos/quill-framework-ii/
http://www.travert-academy.example/lp/php-development-training.aspx?gclid=ZM3rhuPqx51DGTRR8Bpeyk9B2B

Industry/Entity Type

Software

```html
<!DOCTYPE html>
<html lang="en">
<head>
<meta charset="utf-8">
<title>Tom Software Academy</title>
<link rel="stylesheet" href="https://fonts.googleapis.com/css2?family=Arimo:wght@400;700&display=swap">
<style>
:root{
  --orange:#f05a1a;
  --orange-dark:#d2461c;
  --ink:#1e1e1e;
  --text:#222;
  --muted:#7a7a7a;
  --line:#bdbdbd;
  --teal:#52aabf;
  --green:#77a52e;
  --amber:#e0601f;
  --red:#e33232;
  --footer:#dedede;
  --white:#fff;
}
*{box-sizing:border-box;margin:0;padding:0}
html,body{width:1200px;height:862px;overflow:hidden;background:var(--white)}
body{font-family:"Arimo",Arial,sans-serif;color:var(--text)}
.stage{width:1400px;height:1006px;position:relative;transform:scale(.857143);transform-origin:0 0}
.abs{position:absolute}

.brand{left:201px;top:45px;display:flex;align-items:center;gap:14px}
.brand-mark{width:56px;height:56px;border-radius:50%;background:var(--orange)}
.brand-name{font-size:30px;font-weight:700;color:var(--ink);letter-spacing:.5px;line-height:1}

.search{left:861px;top:34px;width:187px;height:27px;border:1px solid var(--line);font-size:12px;color:#777;padding:6px 12px;display:flex;justify-content:space-between;align-items:center}
.social{left:1065px;top:35px;display:flex;gap:9px}
.social span{width:27px;height:27px;border-radius:50%;background:#bdbdbd;display:block}

.nav{top:93px;font-size:13px;font-weight:700;color:var(--ink);letter-spacing:.2px}
.nav a{position:absolute;color:inherit;text-decoration:none;white-space:nowrap}
.nav a.active{color:var(--orange);font-weight:400}

.hero{left:201px;top:136px;width:1000px;height:360px;background:linear-gradient(90deg,#f4f4f4 0%,#ececec 45%,#e0e0e0 100%);overflow:hidden}
.hero-art{position:absolute;left:30px;top:10px;width:460px;height:340px;border-radius:40%;background:radial-gradient(circle at 55% 45%,#d6d6d6 0%,#c4c4c4 35%,#e6e6e6 70%,rgba(236,236,236,0) 100%)}
.hero-badge{position:absolute;left:522px;top:89px;width:123px;height:87px;background:var(--orange)}
.hero-title{position:absolute;left:660px;top:112px;font-size:33px;font-weight:700;color:var(--orange);line-height:1.15;letter-spacing:.5px}
.hero-text{position:absolute;left:526px;top:198px;width:430px;font-size:14px;line-height:24px;color:var(--text)}
.hero-arrows{position:absolute;left:928px;top:313px;display:flex;gap:2px}
.hero-arrows span{width:26px;height:27px;background:var(--orange-dark);display:flex;align-items:center;justify-content:center}

.tiles{left:201px;top:501px;width:1000px;display:flex;gap:1px}
.tile{width:249px;height:244px;color:var(--white);position:relative}
.tile.training{background:var(--teal)}
.tile.development{background:var(--green)}
.tile.consulting{background:var(--amber)}
.tile.course-web{background:var(--red)}
.tile svg.icon{position:absolute;left:50%;top:44px;transform:translateX(-50%)}
.tile h3{position:absolute;left:33px;top:145px;font-size:19px;font-weight:700;letter-spacing:.3px}
.tile p{position:absolute;left:34px;top:172px;font-size:14px;line-height:23px;width:200px}

.about{left:201px;top:778px;width:1000px}
.about h2{font-size:17px;font-weight:400;color:var(--orange);letter-spacing:.2px}
.about p{margin-top:18px;font-size:13px;line-height:24px;color:var(--muted)}

.footer{left:201px;top:945px;width:1000px;height:61px;background:var(--footer);font-size:12px;color:#555;display:flex;align-items:center;justify-content:space-between;padding:0 23px 0 36px}
.footer nav span{margin:0 17px}
</style>
</head>
<body>
<div class="stage">
  <div class="abs brand"><span class="brand-mark"></span><span class="brand-name">TOM Software Academy</span></div>

  <div class="abs search"><span>Search :</span>
    <svg width="15" height="15" viewBox="0 0 15 15" fill="none" stroke="#aaa" stroke-width="1.6"><circle cx="6" cy="6" r="4.6"/><path d="M9.5 9.5 14 14"/></svg>
  </div>
  <div class="abs social"><span></span><span></span><span></span><span></span></div>

  <nav class="abs nav">
    <a class="active" href="#" style="left:667px">HOME</a>
    <a href="#" style="left:770px">TRAINING</a>
    <a href="#" style="left:896px">SERVICING</a>
    <a href="#" style="left:1029px">ABOUT</a>
    <a href="#" style="left:1138px">CONTACT</a>
  </nav>

  <section class="abs hero">
    <div class="hero-art" role="img" aria-label="Businessman pushing a large silver gear"></div>
    <div class="hero-badge"></div>
    <div class="hero-title">TOM SOFTWARE<br>ACADEMY</div>
    <p class="hero-text">We are privileged for being positioned in a region with IT ancestry. Therefore, from short courses to offer specializations to make it more competitive with the labor market and train more competent professionals</p>
    <div class="hero-arrows">
      <span><svg width="10" height="14" viewBox="0 0 10 14" fill="none" stroke="#fff" stroke-width="1.5"><path d="M8 1 2 7l6 6"/></svg></span>
      <span><svg width="10" height="14" viewBox="0 0 10 14" fill="none" stroke="#fff" stroke-width="1.5"><path d="M2 1l6 6-6 6"/></svg></span>
    </div>
  </section>

  <div class="abs tiles">
    <div class="tile training">
      <svg class="icon" width="72" height="70" viewBox="0 0 72 70" fill="#fff"><circle cx="12" cy="8" r="7"/><rect x="2" y="18" width="20" height="30" rx="3"/><rect x="6" y="46" width="6" height="22"/><rect x="14" y="46" width="6" height="22"/><rect x="26" y="4" width="44" height="44" fill="none" stroke="#fff" stroke-width="4"/><path d="M20 30l18-10" stroke="#fff" stroke-width="4"/><path d="M44 50l-8 14M50 50l8 14" stroke="#fff" stroke-width="3"/></svg>
      <h3>TRAINING</h3>
      <p>Click here for know our training Information &#187;</p>
    </div>
    <div class="tile development">
      <svg class="icon" width="62" height="62" viewBox="0 0 62 62" fill="#fff"><rect x="4" y="36" width="14" height="20"/><rect x="22" y="22" width="14" height="34"/><rect x="40" y="6" width="14" height="50"/><rect x="0" y="57" width="60" height="3"/><path d="M58 2v54" stroke="#fff" stroke-dasharray="2 3"/></svg>
      <h3>DEVELOPMENT</h3>
      <p>Click here for know our training Information &#187;</p>
    </div>
    <div class="tile consulting">
      <svg class="icon" width="88" height="68" viewBox="0 0 88 68" fill="none" stroke="#fff" stroke-width="5"><ellipse cx="34" cy="24" rx="30" ry="20"/><path d="M16 40l-6 14 18-10"/><path d="M62 22c12 4 20 12 20 22 0 6-4 11-10 15l4 9-14-6c-10 2-22-1-29-7" fill="#fff" stroke="none" opacity=".95"/></svg>
      <h3>CONSULTING</h3>
      <p>Click here for know our training Information &#187;</p>
    </div>
    <div class="tile course-web">
      <svg class="icon" width="86" height="56" viewBox="0 0 86 56" fill="none" stroke="#fff" stroke-width="4"><rect x="12" y="6" width="62" height="40"/><path d="M2 52h82" stroke-width="5"/></svg>
      <h3>COURSE WEB</h3>
      <p>Click here for know our training Information &#187;</p>
    </div>
  </div>

  <section class="abs about">
    <h2>TOM SOFTWARE ACADEMY</h2>
    <p>It is a long established fact that a reader will be distracted by the readable content of a page when looking at its layout. The point of using Lorem Ipsum is that it has a more-or-less normal distribution of letters, as opposed to using 'Content here, content here', making it look like readable English. Many desktop publishing packages and web page editors now use Lorem Ipsum as their default model text, and a search for 'lorem ipsum' will uncover many web sites still in their infancy. Various versions have evolved over the years, sometimes by accident, sometimes on purpose</p>
  </section>

  <footer class="abs footer">
    <nav>Home<span>|</span>Training<span>|</span>Servicing<span>|</span>About<span>|</span>Contact</nav>
    <div>&copy; Copyright 2014 TOM. All Rights Reserved.</div>
  </footer>
</div>
</body>
</html>
```